We need a PowerPoint to outline what Modeling is about!

PowerPoint presentation to be shown to aspiring models. The students will be joining our 1-day workshop, and they will be taught the very basics of being a model.
What should be included in the slides:
• What is Modelling? - Description of Modelling, and what it takes to be a Model.
• Types of Models in the market - Catwalk Model / Photography Model / Events Model
• Expectations of a model - Professionalism, Punctuality, Confidence, etc etc.
• Practical (catwalk) tips: Posture
• Practical (catwalk) tips: How to do a simple catwalk
• Practical (photography) tips: How to bring out your best angles in photos
• Trainer Assessment of Students
Here are some definitions that we use. You may change the wording as you see fit, as long as the meaning is the same.
Modelling is to promote a product / brand / service in an advertisement, show, commercial or event.
Runway / Fashion Model – Walk the catwalk to promote clothing and accessories in a fashion show.
Most shows require the model to be tall and skinny. Model needs to strut with confidence and grace down the runway. Body shape more important than facial features.
Photography Model – Appear for Print Ads, Magazine Editorials, Posters, etc.
Height requirements are not as strict (or not present) as compared to Runway Model. Good features preferred, but not a must.
Video Model – Appear for TV commercials, Promotional Videos, etc.
Model needs to possess basic acting skills to promote the product, brand or service on video. Confidence and screen charisma more important than looks or body.
Events Model – Promote the product, brand or service during ‘live’ events and shows.
Model needs to be engaging and charismatic to ‘sell’ the product to customers.
A longer description can also be found here: http://www.brightlanecasting.sg/models/
Target Market(s)
Adults aged 18 - 40 who are interested to take up Modeling.
Industry/Entity Type
Events
Requirements
Must have
- Visually appealing! Does not have to be content heavy, but should deliver the message effectively.
Nice to have
- Pretty pictures.

```html
<!DOCTYPE html>
<html lang="en">
<head>
<meta charset="utf-8">
<title>What is Modelling?</title>
<link rel="stylesheet" href="https://fonts.googleapis.com/css2?family=Poiret+One&family=Didact+Gothic&display=swap">
<style>
  :root {
    --ink: #000000;
    --paper: #ffffff;
    --text: #f2f2f2;
    --muted: #9a9a9a;
    --photo-light: #cfcfcf;
    --photo-mid: #6e6e6e;
    --photo-dark: #0c0c0c;
  }
  html, body {
    margin: 0;
    padding: 0;
    overflow: hidden;
    background: var(--ink);
  }
  .slide {
    position: relative;
    width: 1200px;
    height: 871px;
    background: var(--ink);
    overflow: hidden;
  }
  .corner-stripe {
    position: absolute;
    left: 0;
    top: 0;
  }
  .slide-title {
    position: absolute;
    left: 106px;
    top: 116px;
    margin: 0;
    font-family: "Poiret One", sans-serif;
    font-weight: 400;
    font-size: 78px;
    line-height: 1;
    letter-spacing: 2px;
    white-space: nowrap;
    color: var(--paper);
    -webkit-text-stroke: 1.8px var(--paper);
    transform: scaleX(0.79);
    transform-origin: left top;
  }
  .slide-body {
    position: absolute;
    left: 108px;
    top: 284px;
    width: 800px;
    font-family: "Didact Gothic", sans-serif;
    font-size: 25.5px;
    line-height: 27px;
    white-space: nowrap;
    color: var(--text);
  }
  .slide-body p {
    margin: 0 0 27px;
  }
  .hero-photo {
    position: absolute;
    left: 905px;
    top: 310px;
    width: 295px;
    height: 561px;
    background: linear-gradient(160deg, var(--photo-light) 0%, var(--photo-mid) 35%, var(--photo-dark) 80%);
  }
  .brand-name {
    position: absolute;
    left: 26px;
    top: 836px;
    margin: 0;
    font-family: "Didact Gothic", sans-serif;
    font-size: 13px;
    line-height: 1;
    letter-spacing: 1px;
    color: var(--muted);
  }
</style>
</head>
<body>
  <main class="slide">
    <svg class="corner-stripe" width="170" height="130" viewBox="0 0 170 130" aria-hidden="true">
      <line x1="-6" y1="118" x2="160" y2="-6" stroke="#ffffff" stroke-width="13"/>
    </svg>

    <h1 class="slide-title">WHAT IS MODELLING ?</h1>

    <section class="slide-body">
      <p>A MODEL&nbsp; is a person who is employed to promote, display, or<br>
      advertise commercial products (notably fashion clothing) or to serve<br>
      as a visual object for people who are creating works of art.&nbsp; A fashion<br>
      model uses his appearance and natural chemistry to sell goods or<br>
      services.</p>
      <p>He/she commonly works in promotional production settings, including<br>
      still photography sessions, video recording studios and venues<br>
      featuring live fashion shows on runways. Other popular modeling<br>
      environments include specialty stores, retail stores, commercial<br>
      showrooms and custom salons.</p>
    </section>

    <div class="hero-photo" role="img" aria-label="Black and white photograph of a model in a strapless dress, looking to the side"></div>

    <p class="brand-name">Bright Lane Casting</p>
  </main>
</body>
</html>
```